Webdesign für IT-Beratungsdienstleister
Zielgruppe
7K-ADVISA ist spezialisiert auf Fach- und IT-Beratungsdienstleistungen.
Wir unterstützen Unternehmen bei der Leistungsoptimierung durch prozessgetriebene Informationssysteme und Integrationslösungen.
Bitte siehe Aufgaben hier: http://www.7k-advisa.example/ueber-uns/
Zielgruppe sind Mittelständige und sowie Grossunternehmen
Aufgabenstellung
Wordpress template, modern, nicht zu überladen mit der Möglichkeit Beiträge zu veröffentlicehn. Responsive.

```html
<!DOCTYPE html>
<html lang="de">
<head>
<meta charset="utf-8">
<title>7K-ADVISA – Fach- und IT-Beratung</title>
<link rel="stylesheet" href="https://fonts.googleapis.com/css2?family=Ubuntu:ital,wght@0,300;0,400;0,500;0,700;1,400&display=swap">
<style>
:root{
  --orange:#e8650f;
  --orange-light:#f07b24;
  --red:#ec1c24;
  --blue:#0b6fcc;
  --blue-light:#1e88e5;
  --green:#0aa54e;
  --green-light:#16d865;
  --text:#444;
  --muted:#777;
  --dark:#262c37;
  --line:#e3e3e3;
  --panel:#ececec;
}
*{box-sizing:border-box;margin:0;padding:0}
html,body{width:1200px;height:2879px;overflow:hidden}
body{font-family:"Ubuntu",sans-serif;color:var(--text);background:#fff;position:relative}
section,header,footer{position:absolute;left:0;width:1200px}
.abs{position:absolute}
a{color:inherit;text-decoration:none}

/* header */
.site-header{top:0;height:63px;background:#fff;border-bottom:1px solid #ddd}
.brand{position:absolute;display:flex;align-items:center;gap:6px;font-weight:400;letter-spacing:1px}
.brand-dot{width:10px;height:10px;border-radius:50%;background:var(--red)}
.site-header .brand{left:246px;top:14px;font-size:28px;color:#333}
.main-nav{position:absolute;right:248px;top:22px;display:flex;gap:18px;font-size:11px;color:#666}
.main-nav a{padding:3px 7px}
.main-nav a.active{border:1px solid var(--orange);color:var(--orange)}

/* hero */
.hero{top:63px;height:297px;background:linear-gradient(100deg,#5e8aa0 0%,#7fa9bb 40%,#93b5c0 60%,#3b4c66 75%,#6d8fa2 100%)}
.hero-title{left:151px;top:68px;font-size:19px;color:#fff;font-weight:400}
.hero-rule{left:151px;top:98px;width:32px;height:2px;background:var(--red)}
.hero-text{left:151px;top:121px;width:400px;font-size:12.5px;color:#fff;line-height:1.15}
.hero-ask{left:151px;top:163px;font-size:12.5px;color:#fff}
.btn-outline{display:inline-flex;align-items:center;justify-content:center;border:2px solid #fff;color:#fff;font-size:9px;font-weight:500}
.hero .btn-outline{left:151px;top:201px;width:144px;height:23px}
.slide-arrow{top:137px;width:26px;height:26px;background:rgba(255,255,255,.35);border:1px solid rgba(255,255,255,.6)}
.slide-dots{left:580px;top:275px;display:flex;gap:4px}
.slide-dots i{width:7px;height:7px;border-radius:50%;background:#222;border:1px solid #fff}
.slide-dots i:first-child{background:#fff}

/* services */
.services{top:360px;height:416px}
.service-card{top:62px;width:221px;height:293px;border:1px solid var(--line);border-bottom:none;text-align:center}
.service-card h3{font-size:13px;font-weight:400;color:#333;margin-top:15px}
.service-icon{width:126px;height:116px;margin:14px auto 0;border-radius:63px 63px 0 0;background:var(--orange)}
.service-card p{text-align:left;font-size:10px;line-height:1.5;color:#555;padding:0 12px;margin-top:20px}

/* about */
.about{top:776px;height:313px;background:linear-gradient(90deg,#1c2029 0%,#333a47 45%,#4d5564 100%)}
.about-mark{left:255px;top:80px;width:260px;height:140px;background:radial-gradient(ellipse at 60% 50%,rgba(236,28,36,.55),rgba(236,28,36,0) 70%)}
.about h2{left:547px;top:64px;font-size:18px;font-weight:400;color:#fff}
.about p{left:547px;top:115px;width:415px;font-size:12.5px;line-height:1.32;color:#fff}
.about .btn-outline{left:547px;top:225px;width:89px;height:26px}

/* articles */
.articles{top:1089px;height:360px;text-align:center}
.articles h2{position:absolute;left:0;width:1200px;top:38px;font-size:18px;font-weight:400;color:#333}
.articles .rule{left:585px;top:70px;width:30px;height:2px;background:var(--red)}
.post{top:95px;width:227px}
.post-thumb{position:relative;height:128px;background:linear-gradient(160deg,#5a6270 0%,#2e333c 55%,#454b56 100%)}
.read-more{position:absolute;left:-6px;top:98px;background:var(--red);color:#fff;font-size:7px;padding:5px 8px}
.post-meta{text-align:left;font-size:6.5px;font-style:italic;color:#888;margin-top:18px}
.post-meta span{color:var(--orange)}
.post-title{text-align:left;font-size:10px;font-style:italic;color:var(--orange);margin-top:9px}
.btn-orange{left:557px;top:302px;width:85px;height:24px;background:var(--orange);color:#fff;font-size:8.5px;font-weight:500;display:flex;align-items:center;justify-content:center}

/* contact call */
.callout{top:1449px;height:344px;background:linear-gradient(180deg,#7485a0 0%,#8b96a6 35%,#5f6d6a 60%,#2f4a2c 100%)}
.call-box{left:240px;top:106px;width:720px;height:124px}
.call-box h2{left:32px;top:47px;font-size:15px;font-weight:400;color:#fff}
.call-box p{left:32px;top:82px;font-size:9px;color:#ffd8b8}
.call-box .btn-outline{left:573px;top:64px;width:112px;height:22px;font-size:8.5px}

/* offers */
.offers{top:1816px;height:276px}
.offer{top:0;width:240px;height:276px;background:var(--panel)}
.offer-head{height:55px;display:flex;align-items:center;justify-content:center;color:#fff;font-size:15px;font-weight:700}
.offer-sub{position:relative;height:62px;display:flex;align-items:center;justify-content:center;text-align:center;color:#fff;font-size:8.5px;font-weight:700;padding:0 10px}
.offer-sub::after{content:"";position:absolute;bottom:-10px;left:112px;border:8px solid transparent;border-bottom:none;border-top:10px solid var(--c)}
.offer ul{margin:43px 0 0 32px;font-size:9.5px;line-height:1.7;color:#555}
.offer-bc{left:240px;border:1px solid var(--orange)}
.offer-bc .offer-head{background:var(--orange)}
.offer-bc .offer-sub{background:var(--orange-light);--c:var(--orange-light)}
.offer-it{left:480px;border:1px solid var(--blue)}
.offer-it .offer-head{background:var(--blue)}
.offer-it .offer-sub{background:var(--blue-light);--c:var(--blue-light)}
.offer-tc{left:720px;border:1px solid var(--green)}
.offer-tc .offer-head{background:var(--green)}
.offer-tc .offer-sub{background:var(--green-light);--c:var(--green-light)}

/* strip */
.strip{top:2118px;height:100px}
.strip-panel{left:460px;top:3px;width:500px;height:95px}
.strip-brand{left:240px;top:8px;width:232px;height:82px}
.strip-brand .brand{left:24px;top:26px;font-size:24px;color:#fff}
.strip-items{left:480px;top:42px;width:480px;display:flex;justify-content:space-around;font-size:11px;font-weight:700;color:#333}

/* map */
.map{top:2328px;height:314px;background:linear-gradient(120deg,#f4e3cf 0%,#f7caa3 40%,#f3b98b 60%,#f6dcc3 100%)}

/* footer */
.site-footer{top:2642px;height:237px;background:var(--dark);color:#fff}
.site-footer .brand{left:244px;top:36px;font-size:22px;color:#fff}
.footer-about{left:240px;top:74px;width:280px;font-size:7px;line-height:2.2;color:#ddd}
.site-footer h4{font-size:11px;font-weight:700;letter-spacing:.5px}
.footer-links{left:547px;top:36px}
.footer-links ul{list-style:none;margin-top:12px;font-size:7px;line-height:2.3;font-weight:500}
.footer-social{left:793px;top:36px}
.social-list{margin:10px 0 0 7px;display:flex;flex-direction:column;gap:5px}
.social-list i{display:block;width:17px;height:17px;background:#0d0f13}
.footer-rule{left:240px;top:2826px;width:720px;height:3px;background:var(--red);position:absolute}
.copyright{left:0;top:2849px;width:1200px;text-align:center;font-size:8.5px;color:#aaa;position:absolute}
.copyright a{color:#fff}
</style>
</head>
<body>

<header class="site-header">
  <a class="brand" href="#"><span class="brand-dot"></span>7K-ADVISA</a>
  <nav class="main-nav">
    <a class="active" href="#">Home</a><a href="#">Über Uns</a><a href="#">Business Consulting</a><a href="#">IT Consulting</a><a href="#">Training</a><a href="#">Kontakt</a>
  </nav>
</header>

<section class="hero" role="img" aria-label="Foto: Geschäftsmann öffnet sein Hemd vor blauem Himmel">
  <div class="abs slide-arrow" style="left:12px"><svg width="24" height="24"><path d="M14 8l-4 4 4 4" fill="none" stroke="#fff" stroke-width="1.3"/></svg></div>
  <div class="abs slide-arrow" style="right:12px"><svg width="24" height="24"><path d="M10 8l4 4-4 4" fill="none" stroke="#fff" stroke-width="1.3"/></svg></div>
  <h1 class="abs hero-title">7K-ADVISA - Unser Know-How für Ihren Erfolg!</h1>
  <div class="abs hero-rule"></div>
  <p class="abs hero-text">Wir beraten namhafte Unternehmen und stellen individuelle Lösungen zur Verfügung.</p>
  <p class="abs hero-ask">Was dürfen wir für Sie tun?</p>
  <a class="abs btn-outline" href="#">Jetzt kontakt aufnehmen</a>
  <div class="abs slide-dots"><i></i><i></i><i></i><i></i></div>
</section>

<section class="services">
  <article class="abs service-card" style="left:250px">
    <h3>Business Consulting</h3>
    <div class="service-icon" role="img" aria-label="Illustration: Beraterteam"></div>
    <p>Wir unterstützen fachlich Ihre Prozess-optimierungsprojekte mit erstklassiger Beratung für Prozessmanagement, -analyse sowie -implementierung. Wir begleiten Sie bei dem Anforderungs-management, Business Analyse und Projektqualifizierung.</p>
  </article>
  <article class="abs service-card" style="left:489px">
    <h3>IT Consulting</h3>
    <div class="service-icon" role="img" aria-label="Illustration: Arbeitstisch mit Geräten"></div>
    <p>Wir beraten und setzen die IT für Sie um: Technische Prozessimplementierung, Enterprise Architecture, Integration sowie SOA und JEE stellen unsere Kompetenzen dar. Wir bitten customizing von Unternehmenslösungen wie ERP, CRM, SCM an.</p>
  </article>
  <article class="abs service-card" style="left:728px">
    <h3>Training &amp; Coaching</h3>
    <div class="service-icon" role="img" aria-label="Illustration: Tafel mit Zeigestock"></div>
    <p>Auch Querschnittsthemen verlangen eine große Aufmerksamkeit. Wir leisten Unterstützung für Projektmanagement, und diverse Themen wie BPM Methodik &amp; Competence Center, BPMN, SOA, Enterprise Architecture als Berater, Coach, Trainer oder Interimmanager.</p>
  </article>
</section>

<section class="about" role="img" aria-label="Foto: Büroraum, abgedunkelt">
  <div class="abs about-mark" role="img" aria-label="Dekorativer Farbschwung"></div>
  <h2 class="abs">Über Uns</h2>
  <p class="abs">7K-ADVISA ist spezialisiert auf Fach- und IT-Beratungsdienstleistungen. Wir unterstützen Unternehmen bei der Leistungsoptimierung durch prozessgetriebene Informationssysteme. Unsere Kunden vertrauen unseren Full-Service Ansatz, der sich durch hohe Expertise mit fundierten Branchenübergreifenden Erfahrungen sowie Kompetenzen auszeichnet.</p>
  <a class="abs btn-outline" href="#">Mehr erfahren</a>
</section>

<section class="articles">
  <h2>Letzte Artikeln</h2>
  <div class="abs rule"></div>
  <article class="abs post" style="left:247px">
    <div class="post-thumb" role="img" aria-label="Foto: Schreibtisch mit Laptop"><span class="read-more">Read more +</span></div>
    <p class="post-meta">26. November 2016 Von admin in <span>Artikeln</span></p>
    <h3 class="post-title">MusterArtikel</h3>
  </article>
  <article class="abs post" style="left:487px">
    <div class="post-thumb" role="img" aria-label="Foto: Schreibtisch mit Laptop"><span class="read-more">Read more +</span></div>
    <p class="post-meta">26. Oktober 2016 Von admin in <span>Artikeln</span></p>
    <h3 class="post-title">MusterArtikel</h3>
  </article>
  <article class="abs post" style="left:726px">
    <div class="post-thumb" role="img" aria-label="Foto: Schreibtisch mit Laptop"><span class="read-more">Read more +</span></div>
    <p class="post-meta">26. September 2016 Von admin in <span>Artikeln</span></p>
    <h3 class="post-title">MusterArtikel</h3>
  </article>
  <a class="abs btn-orange" href="#">Ältere Artikeln</a>
</section>

<section class="callout" role="img" aria-label="Foto: Stadtansicht mit Fernsehturm, unscharf">
  <div class="abs call-box">
    <svg class="abs" width="720" height="140" style="left:0;top:0"><path d="M0 0L720 18V124H160L152 136L146 124H0Z" fill="#e8650f"/></svg>
    <h2 class="abs">Wir freuen uns immer, von Ihnen zu hören.</h2>
    <p class="abs">Inhaber und Ansprechpartner: Dr. Lorenz Behrendt</p>
    <a class="abs btn-outline" href="#">Kontakt aufnehmen</a>
  </div>
</section>

<section class="offers">
  <div class="abs offer offer-bc">
    <div class="offer-head">Business Consulting</div>
    <div class="offer-sub">Beratung zur fachlichen Prozessoptimierung sowie Business Analyse.</div>
    <ul><li>Prozessmodellierung, -analyse und -Gestaltung</li><li>Business Analyse</li><li>Anforderungsanalyse</li><li>Projektqualifizierung</li><li>BPM / Business Rules</li></ul>
  </div>
  <div class="abs offer offer-it">
    <div class="offer-head">IT Consulting</div>
    <div class="offer-sub">Technologie Beratung im Bezug auf Implementierung und Management.</div>
    <ul><li>Prozessimplementierung</li><li>Enterprise Architecture</li><li>IT- Architecture</li><li>IT- und Applikationsintegration</li><li>BPM / SOA</li><li>Service Management</li></ul>
  </div>
  <div class="abs offer offer-tc">
    <div class="offer-head">Schulung / Coaching</div>
    <div class="offer-sub">Unterstützung als Task-Force für den Projektlauf bzw. Qualifizierung.</div>
    <ul><li>Methodik Schulungen: BPM, BPMN</li><li>Durchführung von Proof of Concept</li><li>Coach für BPM/SOA Competence Center</li></ul>
  </div>
</section>

<section class="strip">
  <svg class="abs strip-panel" width="500" height="95"><path d="M6 0H500L492 95H0Z" fill="#fff" stroke="#ddd"/></svg>
  <div class="abs strip-brand">
    <svg class="abs" width="232" height="82" style="left:0;top:0"><path d="M0 0H232L222 82H0Z" fill="#ec1c24"/></svg>
    <span class="brand">7K-ADVISA</span>
  </div>
  <div class="abs strip-items"><span>Beratung</span><span>Projektmanagement</span><span>Implementierung</span><span>Schulung</span></div>
</section>

<section class="map" role="img" aria-label="Straßenkarte mit Standortmarkierung"></section>

<footer class="site-footer">
  <span class="brand abs">7K-ADVISA</span>
  <p class="abs footer-about">Lorem ipsum dolor sit amet, consetetur sadipscing elitr, sed diam nonumy eirmod tempor invidunt ut labore et dolore magna aliquyam erat, sed diam voluptua. At vero eos et accusam et justo duo dolores et ea rebum.</p>
  <div class="abs footer-links">
    <h4>Links</h4>
    <ul><li>Home</li><li>Über Uns</li><li>Business Consulting</li><li>IT Consulting</li><li>Training</li><li>Kontakt</li></ul>
  </div>
  <div class="abs footer-social">
    <h4>Soziale Netzwerke</h4>
    <div class="social-list"><i></i><i></i><i></i><i></i><i></i></div>
  </div>
</footer>
<div class="footer-rule"></div>
<p class="copyright">Copyright © 2016 7K-ADVISA. | <a href="#">Home</a> | <a href="#">Impressum</a> | <a href="#">Kontakt</a></p>

</body>
</html>
```